I need a business card design for a new company that will be doing consulting work around issues of cultural competency, and diversity and inclusion. I would like the design to be crisp and clear with bold but conservative colors and incorporate shades of blue

Target Market(s)

Small businesses, schools, non-profits

Industry/Entity Type

Consulting

Font styles to use
Serif
Sans Serif

Colors
0c5ba6
6b449b
3276b5
0292cd

Requirements
Must have
• A Morrow Venture (name of company)
• Lemlem Tavish
• CEO
• lemlem@amorrowventure.com
• (215)483-2756

```html
<!DOCTYPE html>
<html lang="en">
<head>
<meta charset="utf-8">
<title>Lemlem Tavish — Business Card</title>
<link rel="stylesheet" href="https://fonts.googleapis.com/css2?family=Poppins:wght@500;600&family=Jost:wght@400;500&display=swap">
<style>
  :root {
    --card-bg: #ffffff;
    --brand-purple: #6a4499;
    --brand-blue: #0c5ba6;
    --accent-blue: #3276b5;
    --sky-blue: #0292cd;
    --name-ink: #ece4e6;
    --contact-ink: #5f5f5f;
  }
  html, body {
    margin: 0;
    padding: 0;
    overflow: hidden;
    background: var(--card-bg);
  }
  .card {
    position: relative;
    width: 1200px;
    height: 686px;
    background: var(--card-bg);
    overflow: hidden;
  }
  .card__panel {
    position: absolute;
    inset: 0;
  }
  .identity {
    position: absolute;
    right: calc(1200px - 466px);
    top: 292px;
    text-align: right;
  }
  .identity__name {
    margin: 0;
    font-family: "Poppins", sans-serif;
    font-weight: 600;
    font-size: 52px;
    line-height: 1;
    letter-spacing: 2px;
    color: var(--name-ink);
  }
  .identity__title {
    margin: 12px 2px 0 0;
    font-family: "Jost", sans-serif;
    font-size: 21px;
    letter-spacing: 1px;
    color: var(--name-ink);
  }
  .contacts {
    position: absolute;
    left: 722px;
    top: 232px;
    margin: 0;
    padding: 0;
    list-style: none;
  }
  .contacts__item {
    display: flex;
    align-items: center;
    height: 50px;
    margin-bottom: 45px;
  }
  .contacts__icon {
    width: 42px;
    height: 42px;
    flex: none;
    display: flex;
    align-items: center;
    justify-content: center;
    color: var(--sky-blue);
  }
  .contacts__icon--at {
    font-family: "Poppins", sans-serif;
    font-weight: 500;
    font-size: 42px;
    line-height: 1;
  }
  .contacts__text {
    margin-left: 31px;
    font-family: "Jost", sans-serif;
    font-size: 22px;
    letter-spacing: 1.3px;
    color: var(--contact-ink);
  }
  .company {
    position: absolute;
    left: 722px;
    top: 548px;
    margin: 0;
    font-family: "Jost", sans-serif;
    font-weight: 500;
    font-size: 24px;
    letter-spacing: 4px;
    text-transform: uppercase;
    color: var(--brand-blue);
  }
</style>
</head>
<body>
<main class="card">
  <svg class="card__panel" width="1200" height="686" viewBox="0 0 1200 686" aria-hidden="true">
    <polygon points="0,0 482,0 650,514 412,686 0,686" fill="var(--accent-blue)"/>
    <polygon points="0,0 466,0 632,511 394,686 0,686" fill="var(--brand-purple)"/>
  </svg>

  <header class="identity">
    <h1 class="identity__name">Lemlem Tavish</h1>
    <p class="identity__title">CEO</p>
  </header>

  <ul class="contacts">
    <li class="contacts__item">
      <span class="contacts__icon" aria-hidden="true">
        <svg width="42" height="34" viewBox="0 0 42 34">
          <path d="M2 11 C2 3 40 3 40 11 L40 14 L30 14 L30 9 C24 7 18 7 12 9 L12 14 L2 14 Z" fill="currentColor"/>
          <path d="M13 15 L29 15 L36 30 L6 30 Z" fill="currentColor"/>
          <circle cx="21" cy="22" r="5.5" fill="var(--card-bg)"/>
          <circle cx="21" cy="22" r="2.5" fill="currentColor"/>
        </svg>
      </span>
      <span class="contacts__text">(215) 483-2756</span>
    </li>
    <li class="contacts__item">
      <span class="contacts__icon contacts__icon--at" aria-hidden="true">@</span>
      <span class="contacts__text">lemlem@amorrowventure.com</span>
    </li>
    <li class="contacts__item">
      <span class="contacts__icon" aria-hidden="true">
        <svg width="38" height="38" viewBox="0 0 38 38" fill="none" stroke="currentColor" stroke-width="1.8">
          <circle cx="19" cy="19" r="17"/>
          <ellipse cx="19" cy="19" rx="8" ry="17"/>
          <line x1="19" y1="2" x2="19" y2="36"/>
          <line x1="2" y1="19" x2="36" y2="19"/>
          <path d="M5 10 H33 M5 28 H33"/>
        </svg>
      </span>
      <span class="contacts__text">www.amorrowventure.com</span>
    </li>
  </ul>

  <p class="company">A Morrow Venture</p>
</main>
</body>
</html>
```